Marcelo Quintana Postcard/Rack Card

Marcelo Quintana
Tenor & Vocal Coach
mqvoice@brivamail.com
(713) 582-6031
www.voicefromthecore.com
Want two sided postcard / rack card.4" x 9"
Front - vertical - picture in t-shirt, name, title (Tenor & Vocal Coach), contact information
Back - horizontal - picture in jacket, name, title (Tenor & Vocal Coach), contact information, bio (see attachment for words)
Do not leave space for an address.
Looking for an edgy modern design!

Target Market(s)

Young adults

Requirements
Nice to have
• Will pay extra to get a complimentary business card design, two sided

```html
<!DOCTYPE html>
<html lang="en">
<head>
<meta charset="utf-8">
<title>Marcelo Quintana – Rack Card &amp; Postcard</title>
<link rel="stylesheet" href="https://fonts.googleapis.com/css2?family=Oswald:wght@300;400;500;600&family=Raleway:wght@500;800&display=swap">
<style>
  :root {
    --stage: #ecebe7;
    --royal-blue: #4a51b6;
    --deep-blue: #3a3f9c;
    --olive: #c9c46b;
    --slate: #7e8b92;
    --navy: #1c2a78;
    --paper: #f4f4f2;
    --white: #ffffff;
  }
  * { box-sizing: border-box; margin: 0; padding: 0; }
  html, body {
    width: 1200px; height: 800px; overflow: hidden;
    background: var(--stage);
  }
  .canvas { position: relative; width: 1200px; height: 800px; }

  .rack-front {
    position: absolute; left: 50px; top: 38px;
    width: 322px; height: 720px;
    box-shadow: 0 3px 10px rgba(0,0,0,.18);
  }
  .postcard-back {
    position: absolute; left: 415px; top: 237px;
    width: 720px; height: 320px;
    box-shadow: 0 3px 10px rgba(0,0,0,.18);
  }
  .card-art { position: absolute; inset: 0; display: block; }

  .front-name {
    font-family: "Raleway", sans-serif; font-weight: 800;
    font-variant: small-caps; letter-spacing: .5px;
    font-size: 22px; fill: var(--navy);
  }
  .front-title {
    font-family: "Raleway", sans-serif; font-weight: 500;
    font-size: 12px; fill: var(--navy);
  }
  .front-contact {
    font-family: "Raleway", sans-serif; font-weight: 500;
    font-size: 12px; fill: var(--white);
  }
  .back-name {
    font-family: "Oswald", sans-serif; font-weight: 600;
    font-size: 21px; fill: var(--navy);
  }
  .back-title {
    font-family: "Oswald", sans-serif; font-weight: 300;
    font-style: italic; font-size: 14px; fill: var(--navy);
  }

  .bio {
    position: absolute; left: 452px; top: 58px; width: 218px;
    font-family: "Oswald", sans-serif; font-weight: 300;
    font-size: 10.6px; line-height: 13.4px; color: var(--white);
  }
  .bio p + p { margin-top: 9px; }
  .bio .contact-line { font-weight: 400; }
  .bio .contact-block { margin-top: 8px; }
</style>
</head>
<body>
<main class="canvas">

  <!-- Front: vertical rack card -->
  <section class="rack-front" aria-label="Rack card front">
    <svg class="card-art" viewBox="0 0 322 720" xmlns="http://www.w3.org/2000/svg">
      <defs>
        <linearGradient id="paperFade" x1="0" y1="0" x2="1" y2="0">
          <stop offset="0" stop-color="#e3e3e3"/>
          <stop offset="1" stop-color="#fafafa"/>
        </linearGradient>
        <radialGradient id="portraitTone" cx=".5" cy=".45" r=".7">
          <stop offset="0" stop-color="#f1efd6"/>
          <stop offset=".55" stop-color="#c9c8b8"/>
          <stop offset="1" stop-color="#6f74b6"/>
        </radialGradient>
      </defs>

      <rect class="paper-base" width="322" height="720" fill="url(#paperFade)"/>
      <polygon class="blue-strip-top" points="262,0 322,0 322,160 250,160" fill="var(--royal-blue)"/>
      <polygon class="olive-panel" points="40,0 282,0 262,150 38,160" fill="var(--olive)"/>

      <g role="img" aria-label="Portrait photo of the tenor in a grey t-shirt, leaning against a wall">
        <rect x="0" y="150" width="322" height="420" fill="url(#portraitTone)"/>
      </g>

      <path class="wave-top" d="M0,162 C80,140 160,138 230,150 C270,157 300,152 322,144 L322,156 C300,164 270,168 230,161 C160,150 80,152 0,172 Z" fill="var(--royal-blue)"/>

      <path class="wave-bottom" d="M0,562 C70,576 150,578 220,568 C270,561 300,560 322,566 L322,720 L0,720 Z" fill="var(--royal-blue)"/>
      <polygon class="paper-bottom-left" points="0,580 48,586 45,720 0,720" fill="url(#paperFade)"/>
      <polygon class="slate-panel" points="48,586 272,570 272,720 45,720" fill="var(--slate)"/>

      <rect class="inner-frame" x="10" y="19" width="302" height="681" fill="none" stroke="#e6e6ee" stroke-width="1.4"/>

      <text class="front-name" x="70" y="92">Marcelo Quintana</text>
      <text class="front-title" x="70" y="112">Tenor &amp; Vocal Coach</text>

      <text class="front-contact" x="165" y="622" text-anchor="middle">mqvoice@brivamail.com</text>
      <g class="phone-icon" transform="translate(109,631)" fill="none" stroke="var(--white)" stroke-width="1.2">
        <circle cx="5" cy="5" r="5"/>
        <path d="M3.3,2.6 C2.6,4.8 4.2,7.6 6.6,8" stroke-linecap="round"/>
      </g>
      <text class="front-contact" x="123" y="640">(713) 582-6031</text>
    </svg>
  </section>

  <!-- Back: horizontal postcard -->
  <section class="postcard-back" aria-label="Postcard back">
    <svg class="card-art" viewBox="0 0 720 320" xmlns="http://www.w3.org/2000/svg">
      <defs>
        <radialGradient id="jacketTone" cx=".5" cy=".35" r=".75">
          <stop offset="0" stop-color="#f0edd2"/>
          <stop offset=".5" stop-color="#b9b39a"/>
          <stop offset="1" stop-color="#2c2f6a"/>
        </radialGradient>
        <linearGradient id="faintFace" x1="0" y1="0" x2="1" y2="0">
          <stop offset="0" stop-color="#4147a4"/>
          <stop offset=".4" stop-color="#5a5fb8"/>
          <stop offset="1" stop-color="#3f45a0"/>
        </linearGradient>
      </defs>

      <rect class="blue-base" width="720" height="320" fill="var(--royal-blue)"/>

      <g role="img" aria-label="Portrait photo of the tenor in a dark jacket and white shirt">
        <rect x="108" y="0" width="285" height="320" fill="url(#jacketTone)"/>
      </g>
      <g role="img" aria-label="Faint blue-toned close-up portrait of the tenor behind the bio">
        <rect x="393" y="0" width="327" height="320" fill="url(#faintFace)"/>
      </g>

      <polygon class="olive-panel" points="0,10 160,32 150,318 0,305" fill="var(--olive)"/>
      <polygon class="slate-panel" points="505,0 715,13 695,320 470,308" fill="var(--slate)"/>

      <text class="back-name" transform="translate(76,230) rotate(-90)">Marcelo Quintana</text>
      <text class="back-title" transform="translate(92,230) rotate(-90)">Tenor &amp; Vocal Coach</text>
    </svg>

    <div class="bio">
      <p>Marcelo is a local singer and actor who has been working professionally around the country as a concert artist and musical theater performer. He studied at the Ridgeway School of Music, Gulf Coast University and works as a vocal coach with local youths and adults in Houston area. Marcelo’s goal is to help his students master their individual instrument so that they can achieve a natural and effortless vocal production.</p>
      <p>For more information please<br>contact Marcelo today!</p>
      <p class="contact-block">
        <span class="contact-line">mqvoice@brivamail.com</span><br>
        <span class="contact-line">&#9990; (713) 582-6031</span>
      </p>
    </div>
  </section>

</main>
</body>
</html>
```